Need logo and design for business card "BrookVale Plumbing Services".

Needing a design for plumbing company 'BrookVale Plumbing Services', a company based on the surfcoast.
Would like the colour black and blue incorporated. We offer free quotes and reliable friendly service, but don't want this writing on front of card.

I do not have a logo so wanting ideas. Any logo ideas on it would be great.

Target Market(s)

People wanting a Plumber

Industry/Entity Type

Business

Requirements
Must have
• Domestic Plumbing
• Commercial Plumbing
• Roofing
• Gasfitting
Nice to have
• Maybe some sort of plumbing picture on it, spanner, toilet, tap with water etc. Just relating to plumbing.
• BrookVale is on word also with the capital A in it.

```html
<!DOCTYPE html>
<html lang="en">
<head>
<meta charset="utf-8">
<title>BrookVale Plumbing Services – Business Card</title>
<link href="https://fonts.googleapis.com/css2?family=Arimo:wght@400;700&display=swap" rel="stylesheet">
<style>
  :root {
    --brand-blue: #02548a;
    --ink: #1e1e1e;
    --frame-grey: #6b6b6b;
    --rule-grey: #555555;
    --tap-grey: #bcbdc0;
    --paper: #ffffff;
  }
  * { margin: 0; padding: 0; box-sizing: border-box; }
  html, body { width: 1200px; height: 1000px; overflow: hidden; background: var(--paper); }
  body { position: relative; font-family: "Arimo", Arial, sans-serif; color: var(--ink); }

  .card-shapes { position: absolute; left: 0; top: 0; }

  .tap-artwork {
    position: absolute; left: 65px; top: 183px; width: 330px; height: 272px;
    background: radial-gradient(ellipse at 60% 45%, #c9cacc 0%, var(--tap-grey) 70%, #a9aaad 100%);
    border-radius: 6px;
  }

  .contact-block {
    position: absolute; right: 72px; top: 180px; text-align: right;
    font-size: 25px; letter-spacing: 3.6px; line-height: 33px;
  }
  .contact-block .name-title { margin-right: 6px; }

  .brand-name {
    position: absolute; left: 473px; top: 405px;
    font-size: 92px; font-weight: 700; color: var(--brand-blue);
    letter-spacing: -1px; line-height: 1;
  }
  .brand-tagline {
    position: absolute; left: 474px; top: 537px;
    font-size: 34px; letter-spacing: 2.6px; line-height: 1;
  }

  .services-list { position: absolute; top: 655px; font-size: 25px; letter-spacing: 3.6px; line-height: 1; }
  .services-list li { list-style: none; position: absolute; white-space: nowrap; }
  .services-list li:nth-child(1) { left: 682px; top: 0; }
  .services-list li:nth-child(2) { left: 734px; top: 41px; }
  .services-list li:nth-child(3) { left: 788px; top: 83px; }

  .hotline {
    position: absolute; left: 148px; width: 400px; top: 748px; text-align: center; color: var(--paper);
  }
  .hotline .vanity-number { font-size: 40px; line-height: 1; letter-spacing: 0.5px; }
  .hotline .web-address { font-size: 33px; line-height: 1; margin-top: 13px; letter-spacing: 0.5px; }
</style>
</head>
<body>
  <svg class="card-shapes" width="1200" height="1000" viewBox="0 0 1200 1000" aria-hidden="true">
    <line x1="0" y1="115" x2="1200" y2="115" stroke="var(--rule-grey)" stroke-width="1"/>
    <line x1="0" y1="895" x2="1200" y2="895" stroke="var(--rule-grey)" stroke-width="1"/>
    <polygon points="0,115 497,675 0,675" fill="var(--brand-blue)"/>
    <rect x="0" y="688" width="585" height="207" fill="var(--brand-blue)"/>
    <rect x="92" y="494" width="26" height="26" fill="var(--paper)"/>
    <rect x="80" y="602" width="51" height="54" fill="var(--paper)"/>
    <rect x="60" y="749" width="87" height="84" fill="var(--paper)"/>
    <rect x="1166" y="178" width="10" height="702" fill="var(--frame-grey)"/>
    <rect x="677" y="862" width="499" height="18" fill="var(--frame-grey)"/>
  </svg>

  <div class="tap-artwork" role="img" aria-label="Grey illustration of a wall tap with handle and round wall plate"></div>

  <div class="contact-block">
    <p class="name-title">Sam Rivers: Master Plumber</p>
    <p>Cell: 555-410-2291</p>
    <p>Office: 555-276-6825</p>
    <p>Fax: 555-410-2299</p>
  </div>

  <div class="brand-name">BrookVale</div>
  <div class="brand-tagline">Plumbing Services</div>

  <ul class="services-list">
    <li>Domestic Plumbing</li>
    <li>Commercial Plumbing</li>
    <li>Roofing &amp; Gas Fitting</li>
  </ul>

  <div class="hotline">
    <p class="vanity-number">555-BROOKVALE</p>
    <p class="web-address">www.brookvale.com</p>
  </div>
</body>
</html>
```